Business Card Design for Small Electrical Contractor

I need to update my business card into something a little more modern. We are a small electrical contracting company. We service domestic and commercial places around Sydney. We have 2 logo designs at the moment. I have uploaded both and 2 different sizes to work with.

Industry/Entity Type

Business

Contact Information for Business Card

Ted Corbin
8/21-23 Holt St, Fernhaven 2087
t - (02) 9471 3820
m - 0427 915 304
E - info@corbinelec.example.au
W - corbinelec.example.au
ABN: 42 907 518 263

Font styles to use
Sans Serif

Requirements
Must have
• I would also like to see the below fit on somewhere aswell
• - Licensed Electrician
• - Level 2 (Cat 1 & 4)
• - Domestic
• - Commercial
• - Repairs and Installations
• - Data
Nice to have
• Try and keep similar colours as logo
Should not have
• No lightning bolts or light globes. Smart and professional please.

```html
<!DOCTYPE html>
<html lang="en">
<head>
<meta charset="utf-8">
<title>Corbin Electrical – Business Card</title>
<link rel="stylesheet" href="https://fonts.googleapis.com/css2?family=Roboto+Condensed:wght@400;700&family=Montserrat:wght@600&display=swap">
<style>
  :root {
    --page: #e9e9e9;
    --card: #0c0c0c;
    --card-edge: #1c1c1c;
    --ink: #ffffff;
    --muted: #e2e2e2;
    --accent: #f5a800;
  }
  * { box-sizing: border-box; margin: 0; padding: 0; }
  html, body {
    width: 1200px; height: 1009px; overflow: hidden;
    background: var(--page);
  }
  .sheet {
    width: 1200px; height: 1009px;
    display: flex; flex-direction: column; align-items: center; justify-content: center;
    gap: 40px;
  }
  .card {
    position: relative;
    width: 720px; height: 440px;
    background: linear-gradient(135deg, var(--card-edge) 0%, var(--card) 55%);
    border-radius: 6px;
    box-shadow: 0 10px 30px rgba(0,0,0,.25);
    color: var(--ink);
  }
  .brand {
    position: absolute; left: 0; right: 0;
    display: flex; align-items: center; justify-content: center; gap: 16px;
    font-family: "Montserrat", sans-serif; font-weight: 600;
    font-size: 46px; letter-spacing: 1px; color: var(--ink);
  }
  .brand-mark { width: 20px; height: 20px; background: var(--accent); }
  .card-front .brand { top: 70px; }
  .card-back .brand { top: 110px; }
  .rule {
    position: absolute; left: 200px; right: 200px; top: 150px;
    height: 2px; background: var(--accent);
  }
  .contact-name {
    position: absolute; left: 0; right: 0; top: 172px; text-align: center;
    font-family: "Roboto Condensed", sans-serif; font-weight: 700;
    font-size: 24px; letter-spacing: 1px; color: var(--ink);
  }
  .contact {
    position: absolute; left: 70px; right: 70px; top: 230px;
    display: grid; grid-template-columns: 1fr 1fr; row-gap: 14px; column-gap: 30px;
    list-style: none;
    font-family: "Roboto Condensed", sans-serif; font-size: 18px; color: var(--muted);
  }
  .contact-item { white-space: nowrap; }
  .contact-item.wide { grid-column: 1 / -1; }
  .contact-label { color: var(--accent); font-weight: 700; margin-right: 8px; }
  .services {
    position: absolute; left: 60px; right: 60px; bottom: 70px;
    display: grid; grid-template-columns: repeat(3, 1fr); row-gap: 26px; column-gap: 20px;
    list-style: none;
    font-family: "Roboto Condensed", sans-serif; font-size: 19px; color: var(--muted);
  }
  .service { display: flex; align-items: center; gap: 12px; white-space: nowrap; }
  .service-icon {
    flex: none; width: 34px; height: 34px; border-radius: 7px;
    background: var(--accent);
    display: flex; align-items: center; justify-content: center;
  }
  .service-icon svg { width: 22px; height: 22px; fill: none; stroke: #111; stroke-width: 2; stroke-linecap: round; stroke-linejoin: round; }
</style>
</head>
<body>
<main class="sheet">
  <section class="card card-front" aria-label="Card front">
    <div class="brand"><span class="brand-mark"></span>Corbin Electrical</div>
    <div class="rule"></div>
    <p class="contact-name">Ted Corbin</p>
    <ul class="contact">
      <li class="contact-item wide"><span class="contact-label">A</span>8/21-23 Holt St, Fernhaven 2087</li>
      <li class="contact-item"><span class="contact-label">t</span>(02) 9471 3820</li>
      <li class="contact-item"><span class="contact-label">m</span>0427 915 304</li>
      <li class="contact-item"><span class="contact-label">E</span>info@corbinelec.example.au</li>
      <li class="contact-item"><span class="contact-label">W</span>corbinelec.example.au</li>
      <li class="contact-item wide"><span class="contact-label">ABN</span>42 907 518 263</li>
    </ul>
  </section>

  <section class="card card-back" aria-label="Card back">
    <div class="brand"><span class="brand-mark"></span>Corbin Electrical</div>
    <ul class="services">
      <li class="service">
        <span class="service-icon"><svg viewBox="0 0 24 24"><rect x="5" y="3" width="14" height="18" rx="2"/><path d="M9 8h6M9 12h6M9 16h4"/></svg></span>
        Licensed Electrician
      </li>
      <li class="service">
        <span class="service-icon"><svg viewBox="0 0 24 24"><circle cx="12" cy="9" r="5"/><path d="M9 13l-2 8 5-3 5 3-2-8"/></svg></span>
        Level 2 (Cat 1 &amp; 4)
      </li>
      <li class="service">
        <span class="service-icon"><svg viewBox="0 0 24 24"><path d="M3 11l9-7 9 7"/><path d="M6 10v10h12V10"/><path d="M10 20v-5h4v5"/></svg></span>
        Domestic
      </li>
      <li class="service">
        <span class="service-icon"><svg viewBox="0 0 24 24"><rect x="4" y="4" width="16" height="17"/><path d="M8 8h2M14 8h2M8 12h2M14 12h2M10 21v-4h4v4"/></svg></span>
        Commercial
      </li>
      <li class="service">
        <span class="service-icon"><svg viewBox="0 0 24 24"><path d="M14 6a4 4 0 0 0 5 5l-9 9a2 2 0 0 1-3-3l9-9a4 4 0 0 0-2-2z"/></svg></span>
        Repairs and Installations
      </li>
      <li class="service">
        <span class="service-icon"><svg viewBox="0 0 24 24"><path d="M5 12l5 5 9-10"/></svg></span>
        Data
      </li>
    </ul>
  </section>
</main>
</body>
</html>
```